Business card for our large format printing and installation business

We want a professional looking business card for our business. We manufacture and install Signs.

On the back of the card add this info
Large Format Graphics Printing & Installations, Event Graphics, Banners, Posters, Vehicle Fleet Graphics, Boat Wraps, Wall Murals, Decals,Displays,Signs,Plaques,Digital Signs

On the Front of the card add the Tallmoor Signs logo, plus On the back of the card add the Orange Tallmoor Wraps logo. The 2 vector logos are attached to the design brief.

Target Market(s)

Local business owners

Contact Information for Business Card

Colors
f37122
f68d4e
f9ba93

Requirements
Must have
• On the Front of the card add the Tallmoor Signs logo, plus On the back of the card add the Orange Tallmoor Wraps logo. The 2 vector logos are attached to the design brief.

```html
<!DOCTYPE html>
<html lang="en">
<head>
<meta charset="utf-8">
<title>Tallmoor Business Card</title>
<link href="https://fonts.googleapis.com/css2?family=Exo+2:wght@400;600;800&display=swap" rel="stylesheet">
<style>
  :root {
    --backdrop: #4b4a49;
    --card: #282626;
    --yellow: #f7c51e;
    --amber: #f5ad21;
    --orange: #f37122;
    --orange-soft: #f68d4e;
    --white: #f2f2f2;
    --ghost: #353230;
  }
  * { margin: 0; padding: 0; box-sizing: border-box; }
  html, body { width: 1200px; height: 900px; overflow: hidden; }
  body {
    background: var(--backdrop);
    font-family: "Exo 2", sans-serif;
    position: relative;
  }
  .card {
    position: absolute;
    left: 311px;
    width: 577px;
    height: 329px;
    background: var(--card);
    overflow: hidden;
  }
  .card--services { top: 98px; }
  .card--contact { top: 472px; }

  .ghost-name {
    position: absolute;
    left: -8px; top: 58px;
    width: 600px;
    font-weight: 800;
    font-size: 118px;
    line-height: 0.9;
    color: var(--ghost);
    white-space: nowrap;
  }
  .brand-name {
    position: absolute;
    font-weight: 800;
    color: var(--amber);
    text-align: center;
    line-height: 0.95;
  }
  .card--services .brand-name {
    left: 0; width: 577px; top: 108px;
    font-size: 50px;
  }
  .service-list {
    position: absolute;
    left: 0; top: 253px; width: 577px;
    text-align: center;
    font-weight: 600;
    font-size: 15.5px;
    line-height: 19.5px;
  }
  .service-list .line-1 { color: var(--yellow); }
  .service-list .line-2 { color: #f6b820; }
  .service-list .line-3 { color: #f4a322; }

  .card--contact .brand-name {
    left: 28px; width: 240px; top: 124px;
    font-size: 36px;
  }
  .divider {
    position: absolute;
    left: 287px; top: 77px;
    width: 2px; height: 174px;
    background: var(--orange);
  }
  .contact {
    position: absolute;
    left: 324px; top: 72px;
  }
  .contact__name {
    font-weight: 600;
    font-size: 19px;
    color: var(--amber);
    margin-bottom: 14px;
  }
  .contact__address {
    font-size: 15.5px;
    line-height: 24px;
    color: var(--orange);
    margin-bottom: 8px;
  }
  .contact__row {
    display: flex;
    align-items: center;
    gap: 8px;
    font-size: 15px;
    line-height: 22.5px;
    color: var(--white);
  }
  .contact__row svg { width: 14px; height: 14px; flex: none; }
  .contact__label { color: var(--orange); }
  .accent-band {
    position: absolute;
    left: 0; bottom: 0;
    width: 100%; height: 15px;
    background: linear-gradient(180deg, var(--yellow), var(--amber));
  }
</style>
</head>
<body>

<section class="card card--services">
  <div class="ghost-name" aria-hidden="true">Tallmoor<br>&nbsp;&nbsp;&nbsp;&nbsp;Wraps</div>
  <div class="brand-name">Tallmoor<br>Wraps</div>
  <p class="service-list">
    <span class="line-1">Large Format Graphics Printing &amp; Installations &nbsp;|&nbsp; Event Graphics</span><br>
    <span class="line-2">Banners Posters &nbsp;|&nbsp; Vehicle Fleet Graphics &nbsp;|&nbsp; Boat Wraps &nbsp;|&nbsp; Wall</span><br>
    <span class="line-3">Murals &nbsp; Decals &nbsp;|&nbsp; Displays &nbsp;|&nbsp; Signs &nbsp;|&nbsp; Plaques &nbsp;|&nbsp; Digital Signs</span>
  </p>
</section>

<section class="card card--contact">
  <div class="brand-name">Tallmoor<br>Signs</div>
  <div class="divider"></div>
  <div class="contact">
    <p class="contact__name">Marco Delvane</p>
    <p class="contact__address">1480 Harbor Mill Road #7<br>Seabrook Cove, FL 33190</p>
    <p class="contact__row">
      <svg viewBox="0 0 16 16"><path fill="#f5ad21" d="M3.6 1.2l2.3 2.9-1.3 1.6c.9 2 2.7 3.8 4.7 4.7l1.6-1.3 2.9 2.3-1.1 2.4C7 13.5 2.5 9 1.2 4.3z"/></svg>
      <span>555-310-4827 <span class="contact__label">(Office)</span></span>
    </p>
    <p class="contact__row">
      <svg viewBox="0 0 16 16"><path fill="#f5ad21" d="M3.6 1.2l2.3 2.9-1.3 1.6c.9 2 2.7 3.8 4.7 4.7l1.6-1.3 2.9 2.3-1.1 2.4C7 13.5 2.5 9 1.2 4.3z"/></svg>
      <span>555-628-9143 <span class="contact__label">(Direct)</span></span>
    </p>
    <p class="contact__row">
      <svg viewBox="0 0 16 16"><rect x="1" y="3" width="14" height="10" rx="1" fill="#f5ad21"/><path d="M1.5 3.8L8 9l6.5-5.2" fill="none" stroke="#282626" stroke-width="1.3"/></svg>
      <span>marco@tallmoor.net</span>
    </p>
    <p class="contact__row">
      <svg viewBox="0 0 16 16"><g fill="none" stroke="#f5ad21" stroke-width="1.4"><circle cx="8" cy="8" r="6.3"/><ellipse cx="8" cy="8" rx="2.6" ry="6.3"/><path d="M1.7 8h12.6"/></g></svg>
      <span>www.Tallmoorwraps.com</span>
    </p>
  </div>
  <div class="accent-band"></div>
</section>

</body>
</html>
```